Tails of Comfort Therapy & Dog Training

I have a dual themed business. I am a nationally recognized dog trainer for NHF (National Hound Federation) and Animal Allies (Pet Therapy). One side of my business card will need to address my pet therapy ministry called "Tails of Comfort Therapy". We visit almost 1,000 people a month bringing emotionally uplifting happy visits for nursing homes, veterans hospitals, hospice care, surgery recovery, school systems, and libraries, etc. In addition to emotionally positive effects, pet therapy also helps with anxiety, mobility, regulating blood pressure, and many more advantages. I've attached 2 graphics that are connected with this ministry; #1 paw print inside ribbon heart, #2 clasping hands sketch. The story behind the clasping hands is that it is an actual picture of my hand holding my mother's hand on her death bed (with a sketch filter used). My mother lived in a different state than I live in, and I had wished she had pet therapy available to her in her last months of life. They would have provided some bright moments to her difficult days. So, I vowed that although I was not able to help my own mother, I could train my own dog to reach out to hundreds of people in the community I live in. I have continued to live up to that vow, and have gone on to become a national trainer for other people who would like to train their pets to do the same thing.SIDE TWO of my business card will be announcing that I am a dog trainer for puppies, basic obedience, pet therapy, ESA (emotional support animals), and service dogs. Additionally, I offer canine body language training, dog agility training, and cognitive training. I have also attached two graphics for this side: #1 NHF logo, #2 Animal Allies Evaluation

Target Market(s)

Industry/Entity Type

Dog Training

Contact Information for Business Card

I'm looking for a designer who is good with color scheme & fonts.
2-sided card
one side for pet therapy
one side for dog training

Logo Text

Tails of ComfortTherapy

Font styles to use
Sans Serif
Decorative

Colors

Designer to choose colors to be used in the design.

Requirements
Must have
• -Contact information: Marla Quince (555) 203-9164
• - Contact information for online: Tails of Comfort Therapy (Facebook, Instagram & Twitter)
• - Graphics for pet therapy: clasping hands
• - Graphics for dog training: NHF Model Neighbor Dog, Animal Allies
• - List of dog training classes I offer: Basic Obedience, NHF Model Neighbor Dog, NHF B.R.I.G.H.T. Pup, Pet Therapy training, ESA (Emotional Support Animal), Service Dog training, Canine Body Language, Dog Agility, Cognitive Training, Dog Trick Training
Nice to have
• appealing graphic for dog training school
• Titles in decorative font (but still easy to read) & detail info in very easy to read font

```html
<!DOCTYPE html>
<html lang="en">
<head>
<meta charset="utf-8">
<title>Tails of Comfort Therapy – Business Card</title>
<link href="https://fonts.googleapis.com/css2?family=Open+Sans:wght@400;600;700&display=swap" rel="stylesheet">
<style>
  :root {
    --backdrop: #2b2b2d;
    --card: #f7f7f7;
    --card-shade: #e9e9ea;
    --ink: #2a2a2c;
    --rose: #c81d5c;
    --brown: #4a3a26;
    --badge-blue: #2f5fa8;
    --badge-gold: #e8c438;
    --faint: #dcdcde;
  }
  * { box-sizing: border-box; margin: 0; padding: 0; }
  html, body { width: 1200px; height: 900px; overflow: hidden; }
  body {
    background: var(--backdrop);
    font-family: "Open Sans", Arial, sans-serif;
    position: relative;
  }
  .card {
    position: absolute;
    width: 630px;
    height: 360px;
    border-radius: 34px;
    background: radial-gradient(ellipse at 45% 35%, #ffffff 0%, var(--card) 55%, var(--card-shade) 100%);
    box-shadow: 0 18px 40px rgba(0,0,0,.45);
    overflow: hidden;
  }
  .card--front { left: 120px; top: 70px; }
  .card--back  { left: 450px; top: 470px; }

  /* front */
  .front__watermark {
    position: absolute;
    left: 170px; top: 30px;
    width: 290px; height: 270px;
    border-radius: 50%;
    background: radial-gradient(circle, rgba(200,200,204,.45) 0%, rgba(220,220,222,.15) 60%, rgba(255,255,255,0) 75%);
  }
  .front__brand {
    position: absolute;
    left: 0; right: 0; top: 100px;
    text-align: center;
  }
  .brand__mark {
    display: inline-block;
    width: 46px; height: 46px;
    border-radius: 50%;
    background: var(--rose);
    margin-bottom: 10px;
  }
  .brand__name {
    font-weight: 700;
    font-size: 38px;
    color: var(--ink);
    line-height: 1;
    letter-spacing: -0.5px;
  }
  .brand__sub {
    font-size: 16px;
    letter-spacing: 20px;
    color: var(--rose);
    margin-top: 8px;
    padding-left: 20px;
  }
  .front__person {
    position: absolute;
    left: 0; right: 0; top: 225px;
    text-align: center;
    font-size: 22px;
    color: var(--rose);
  }
  .front__contacts {
    position: absolute;
    left: 60px; right: 40px; top: 275px;
    display: flex; align-items: center; gap: 28px;
    font-size: 14px; color: var(--ink);
  }
  .contact { display: flex; align-items: center; gap: 7px; }
  .contact__square { width: 12px; height: 12px; background: var(--rose); border-radius: 2px; }
  .icon-phone { width: 16px; height: 16px; fill: var(--rose); }

  /* back */
  .back__name {
    position: absolute; left: 0; right: 0; top: 85px;
    text-align: center;
    font-weight: 600; font-size: 25px; color: var(--ink);
  }
  .back__services {
    position: absolute; left: 90px; right: 40px; top: 135px;
    font-size: 16px; color: var(--rose); line-height: 1.55;
  }
  .back__phone {
    position: absolute; left: 90px; top: 280px;
    display: flex; align-items: center; gap: 10px;
    font-size: 19px; color: var(--ink);
  }
  .back__phone .icon-phone { width: 20px; height: 20px; }
  .back__partners {
    position: absolute; right: 50px; top: 200px;
    display: flex; align-items: center; gap: 18px;
  }
  .partner-name {
    font-weight: 700; font-size: 20px; color: var(--brown);
    display: flex; align-items: center; gap: 8px;
  }
  .partner-name__dot { width: 30px; height: 30px; border-radius: 50%; background: var(--rose); }
  .badge { width: 70px; height: 70px; }
</style>
</head>
<body>

<section class="card card--front" aria-label="Pet therapy side">
  <div class="front__watermark" role="img" aria-label="Faint large paw and clasping hands emblem"></div>
  <div class="front__brand">
    <span class="brand__mark"></span>
    <div class="brand__name">Tails of Comfort</div>
    <div class="brand__sub">THERAPY</div>
  </div>
  <div class="front__person">Your Name</div>
  <div class="front__contacts">
    <span class="contact">
      <svg class="icon-phone" viewBox="0 0 24 24"><path d="M6.6 10.8a15.1 15.1 0 0 0 6.6 6.6l2.2-2.2a1 1 0 0 1 1-.25 11.4 11.4 0 0 0 3.6.57 1 1 0 0 1 1 1V20a1 1 0 0 1-1 1A17 17 0 0 1 3 4a1 1 0 0 1 1-1h3.5a1 1 0 0 1 1 1c0 1.25.2 2.45.57 3.57a1 1 0 0 1-.25 1z"/></svg>
      000 000 0000
    </span>
    <span class="contact"><span class="contact__square"></span>/yourinstagram</span>
    <span class="contact"><span class="contact__square"></span>/yourfacebook</span>
  </div>
</section>

<section class="card card--back" aria-label="Dog training side">
  <div class="back__name">Your Name</div>
  <p class="back__services">
    Dog trainer for puppies &nbsp;|&nbsp; Basic obedience &nbsp;|&nbsp; Pet therapy &nbsp;|&nbsp; ESA<br>
    Dog agility training and Cognitive training &nbsp;|&nbsp; Canine Body Language
  </p>
  <div class="back__phone">
    <svg class="icon-phone" viewBox="0 0 24 24"><path d="M6.6 10.8a15.1 15.1 0 0 0 6.6 6.6l2.2-2.2a1 1 0 0 1 1-.25 11.4 11.4 0 0 0 3.6.57 1 1 0 0 1 1 1V20a1 1 0 0 1-1 1A17 17 0 0 1 3 4a1 1 0 0 1 1-1h3.5a1 1 0 0 1 1 1c0 1.25.2 2.45.57 3.57a1 1 0 0 1-.25 1z"/></svg>
    000 000 0000
  </div>
  <div class="back__partners">
    <span class="partner-name"><span class="partner-name__dot"></span>Animal Allies</span>
    <svg class="badge" viewBox="0 0 70 70" role="img" aria-label="Model Neighbor Dog evaluator badge">
      <circle cx="35" cy="35" r="33" fill="var(--badge-gold)"/>
      <circle cx="35" cy="35" r="24" fill="var(--badge-blue)"/>
    </svg>
  </div>
</section>

</body>
</html>
```